Company Corporate Profile Brochure for IT Infrastructure Company

Create new corporate profile presentation deck (ie in a format that can be presented in power point) . We are a growing regional IT infrastructure company across Asia Pacific. We need to show case our projects and install abilities for Structure Cabling, Audio Visual and Physical Security (later to lesser extent). I am looking to improve and make look professional the attached current power point. I would like project profile slides that can be customised depending on the country of the prospect. ie If we are bidding a project in the Philippines, we have slides show casing Philippines works, plus our set of high profile projects from other countries. Key Slides for the presentation:-- Company Background- Install Capability + Industry Certifications- Methodology- Project Examples- Key Personnel & Experience- Contact Details.
Target Market(s)
IT Directors, Designers, Real Estate Project Managers
Industry/Entity Type
It Company
Requirements
Must have
- Design in a format that it can be presented as slide presentation.
- About us
- What we do
- Certifications
- Project Profiles
- Key Personnel Profiles

```html
<!DOCTYPE html>
<html lang="en">
<head>
<meta charset="utf-8">
<title>Northvale Corporate Profile Deck</title>
<link href="https://fonts.googleapis.com/css2?family=Montserrat:wght@500;700;800&family=Roboto+Condensed:wght@400;700&display=swap" rel="stylesheet">
<style>
:root{
  --bg:#332f2d;
  --navy:#2b3a8f;
  --blue:#2f45a3;
  --orange:#f7941d;
  --gold:#c9b81c;
  --ink:#3a3a3a;
  --white:#ffffff;
  --rule:#2b3a8f;
}
*{box-sizing:border-box;margin:0;padding:0}
html,body{width:1200px;height:1200px;overflow:hidden;background:var(--bg)}
.canvas{position:relative;width:1200px;height:1200px;background:var(--bg);font-family:"Roboto Condensed",sans-serif;color:var(--ink)}
.slide{position:absolute;width:267px;height:150px;background:var(--white);overflow:hidden}
.abs{position:absolute}
.heading{position:absolute;left:13px;top:11px;font:800 7.6px "Montserrat",sans-serif;color:var(--navy);letter-spacing:.1px;white-space:nowrap}
.heading .lead{border-bottom:1px solid var(--orange);padding-bottom:1px}
.foot-line{position:absolute;left:0;top:140px;width:198px;height:.7px;background:var(--rule)}
.foot-line::after{content:"";position:absolute;left:0;top:0;width:28px;height:.7px;background:var(--orange)}
.mark{position:absolute;font:700 6px "Montserrat",sans-serif;color:var(--navy);letter-spacing:.3px;white-space:nowrap}
.foot-mark{left:202px;top:136px}
.tiny{font-size:3.6px;line-height:4.6px;color:var(--ink)}
.photo{position:absolute}
/* cover */
.cover .photo{inset:0;background:linear-gradient(120deg,#8d93b4 0%,#5c67a6 35%,#3446a0 70%,#2b3d9c 100%)}
.cover .mark{left:134px;top:37px;font-size:11px;color:var(--white);letter-spacing:.6px}
.welcome{position:absolute;left:170px;top:112px;display:flex;gap:4px;align-items:center;color:var(--white)}
.welcome b{display:block;font:700 6.4px "Montserrat",sans-serif}
.welcome span{display:block;font:500 6.2px "Montserrat",sans-serif;color:#dfe3f5}
/* intro */
.intro .mark{left:0;width:267px;text-align:center;top:26px;font-size:11px}
.intro .tagline{position:absolute;left:0;width:267px;top:47px;text-align:center;font-size:4.6px}
.tiles{position:absolute;left:6px;top:75px;display:flex;gap:4px}
.tile{width:49px;height:43px;border:1.2px solid var(--gold);background:var(--gold);display:flex;flex-direction:column}
.tile i{display:block;height:33px;background:linear-gradient(135deg,#9aa0a8,#d7dadf)}
.tile.blue i{background:linear-gradient(135deg,#2e5ab8,#a8c0ea)}
.tile span{font:700 3.3px "Roboto Condensed",sans-serif;color:var(--navy);text-align:center;line-height:3.6px;padding-top:.5px}
.intro-rule{position:absolute;left:0;right:0;top:130px;height:.6px;background:#555}
.intro-web{position:absolute;top:138px;font-size:4.2px}
/* agenda */
.agenda-item{position:absolute;display:flex;align-items:center;gap:3px}
.num{width:10px;height:10px;border-radius:50%;background:var(--orange);color:var(--white);font:700 4px "Montserrat",sans-serif;display:flex;align-items:center;justify-content:center}
.agenda-item span{font-size:4.2px;line-height:4.6px;text-transform:uppercase}
/* about */
.about .photo{left:0;top:0;width:106px;height:150px;background:linear-gradient(160deg,#e9e9e9,#9c9c9c 55%,#4a4a4a)}
.about .heading{left:114px}
.about .text{position:absolute;left:114px;top:30px;width:146px}
.about .text p{margin-bottom:2px}
.badge{position:absolute;top:131px;width:11px;height:11px;border-radius:50%;background:var(--orange);border:1.4px solid var(--gold)}
/* solutions */
.sol-icon{position:absolute;top:28px;width:32px;height:32px;border-radius:50%;border:1px solid var(--orange)}
.sol-col{position:absolute;top:61px}
.sol-col h4{font:700 4.2px "Roboto Condensed",sans-serif;color:var(--navy);margin-bottom:2px}
.sol-col li{list-style:none;font-size:4.6px;line-height:8.2px}
.sol-col li::before{content:"•";color:var(--orange);margin-right:1px}
/* brands */
.brand{position:absolute;font:800 8px "Montserrat",sans-serif;color:var(--navy);white-space:nowrap}
.brand-box{position:absolute;border:.6px solid #666;font-size:3.7px;line-height:4.2px;text-align:center;color:#555}
.screen{position:absolute;left:101px;top:68px;width:52px;height:33px;background:linear-gradient(180deg,#20263a,#5b5f78);border:1.5px solid #222}
/* break */
.break{background:var(--blue);color:var(--white);text-align:center}
.break .lets{position:absolute;left:0;right:0;top:104px;font:500 7px "Montserrat",sans-serif;color:#cfd6f3}
.break .big{position:absolute;left:0;right:0;top:111px;font:800 12.5px "Montserrat",sans-serif}
.break .mins{position:absolute;left:0;right:0;top:130px;font:700 2.8px "Montserrat",sans-serif;letter-spacing:1px;color:#13207a}
/* team */
.person{position:absolute;width:18px;height:18px;border-radius:50%;background:radial-gradient(circle at 50% 40%,#e1c9b2,#9a7d67);border:1px solid var(--orange)}
.pname{position:absolute;font:700 3.6px "Roboto Condensed",sans-serif;line-height:3.8px;color:var(--ink);white-space:nowrap}
.pname small{display:block;font-weight:400;font-size:2.8px}
/* clients */
.clients .text{position:absolute;left:88px;top:37px;width:166px;font-size:4.6px;line-height:6.2px}
.clients .link{position:absolute;left:88px;top:112px;font-size:5.6px;line-height:7px;color:var(--navy)}
.clients .link b{font-weight:700}
/* projects */
.proj{position:absolute;top:27px;width:73px}
.proj-img{height:23px;position:relative;background:linear-gradient(90deg,#2b3a8f 0%,#4f63b8 45%,#9fb0d8 100%)}
.proj-img span{position:absolute;left:2px;top:5px;color:var(--white);font:700 5px "Roboto Condensed",sans-serif;line-height:5px}
.proj-img span small{display:block;font-weight:400;font-size:3px;line-height:3.6px;color:#d8def5}
.proj .meta{font-size:3.2px;line-height:3.9px;margin-top:2px;color:var(--navy);font-weight:700}
.proj ul{list-style:none;font-size:3.1px;line-height:3.9px;color:#444}
.proj li.b::before{content:"•";color:var(--orange);margin-right:1px}
/* safety / why */
.bullets{position:absolute;list-style:none}
.bullets li{position:relative;padding-left:4px}
.bullets li::before{content:"•";position:absolute;left:0}
.safety .bullets{left:88px;top:40px;width:168px;font-size:3.6px;line-height:4.6px}
.safety .intro-line{position:absolute;left:88px;top:33px;font-size:3.6px}
.why .bullets{left:86px;top:32px;width:168px;font-size:4.4px;line-height:5.9px}
.why .bullets li{margin-bottom:2.4px}
.handshake{position:absolute;left:12px;top:61px;width:56px;height:44px;border-radius:6px;background:linear-gradient(135deg,#dfe4f5,#b9c3ea)}
/* thanks */
.thanks .title{position:absolute;left:0;right:0;top:12px;text-align:center;font:800 29px "Montserrat",sans-serif;color:var(--navy);letter-spacing:-.5px}
.thanks .mark{left:0;width:267px;text-align:center;top:55px;font-size:11px}
.office{position:absolute;top:83px;width:42px;text-align:center;font-size:4.6px;line-height:5.4px}
.flag{width:13px;height:13px;border-radius:50%;margin:0 auto 2px;background:#d8202a;border:.8px solid #bbb}
.thanks .rule{position:absolute;left:0;right:0;top:130px;height:.6px;background:#555}
.thanks .web{position:absolute;top:136px;font-size:4.2px}
</style>
</head>
<body>
<div class="canvas">

  <section class="slide cover" style="left:315px;top:114px">
    <div class="photo" role="img" aria-label="Misty cable-stayed bridge photograph in blue tones"></div>
    <div class="mark">NORTHVALE</div>
    <div class="welcome">
      <svg width="12" height="12" viewBox="0 0 12 12"><circle cx="6" cy="6" r="5.3" fill="none" stroke="#fff" stroke-width=".8"/><path d="M3 6h6M6.5 3.5 9 6l-2.5 2.5" fill="none" stroke="#fff" stroke-width=".8"/></svg>
      <div><b>Welcome to</b><span>Our Presentations</span></div>
    </div>
  </section>

  <section class="slide intro" style="left:618px;top:114px">
    <div class="mark">NORTHVALE</div>
    <p class="tagline">A leading provider of business technology solutions across Asia Pacific.</p>
    <div class="tiles">
      <div class="tile blue"><i role="img" aria-label="Server rack photograph"></i><span>IT<br>INFRASTRUCTURE</span></div>
      <div class="tile"><i role="img" aria-label="Cabling cabinet photograph"></i><span>STRUCTURED<br>CABLING</span></div>
      <div class="tile"><i role="img" aria-label="Meeting room photograph"></i><span>AUDIO<br>VISUAL</span></div>
      <div class="tile"><i role="img" aria-label="Card access reader photograph"></i><span>SECURITY ACCESS<br>CONTROL</span></div>
      <div class="tile"><i role="img" aria-label="Electrical work photograph"></i><span>ELECTRICAL</span></div>
    </div>
    <div class="intro-rule"></div>
    <div class="intro-web" style="left:60px">www.northvale.com</div>
    <div class="intro-web" style="left:156px">info@northvale.com</div>
  </section>

  <section class="slide agenda" style="left:132px;top:336px">
    <h2 class="heading"><span class="lead">OUR</span> AGENDA</h2>
    <div class="agenda-item" style="left:37px;top:40px"><div class="num">01</div><span>About<br>Us</span></div>
    <div class="agenda-item" style="left:37px;top:64px"><div class="num">02</div><span>Our<br>Solutions</span></div>
    <div class="agenda-item" style="left:37px;top:89px"><div class="num">03</div><span>Cabling<br>Supply &amp; Install</span></div>
    <div class="agenda-item" style="left:37px;top:113px"><div class="num">04</div><span>AV Supply<br>&amp; Install</span></div>
    <div class="agenda-item" style="left:151px;top:40px"><div class="num">05</div><span>Our<br>Clients</span></div>
    <div class="agenda-item" style="left:151px;top:64px"><div class="num">06</div><span>Project<br>Experience</span></div>
    <div class="agenda-item" style="left:151px;top:89px"><div class="num">07</div><span>Health &amp; Safety<br>Statement</span></div>
    <div class="agenda-item" style="left:151px;top:113px"><div class="num">08</div><span>Why Choose<br>Northvale?</span></div>
    <div class="foot-line"></div><div class="mark foot-mark">NORTHVALE</div>
  </section>

  <section class="slide about" style="left:467px;top:336px">
    <div class="photo" role="img" aria-label="Black and white boardroom photograph"></div>
    <h2 class="heading"><span class="lead">ABO</span>UT US</h2>
    <div class="text tiny">
      <p>Northvale is a leading provider of business technology solutions in Asia Pacific since 2004 with a blue chip client list that includes Orchard Labs, Halden Bank, RideLink, Workhive.</p>
      <p>We have offices in Singapore, Hong Kong, Malaysia, New Zealand &amp; Australia.</p>
      <p>We specialise in complete IT solutions for hotels, commercial offices, trading rooms, educational institutions, and data centres.</p>
      <p>Northvale staff hold relevant industry certifications to support all Audio Visual and Structured Cabling works. We are a certified member of our AV association, the leading resource for AV standards, certification, training, market intelligence and thought leadership.</p>
      <p>We have a strong track record of implementation capability with signature projects deployed in Australia, New Zealand, China, Myanmar, Indonesia, India, Singapore, Malaysia, Thailand, Hong Kong, South Korea, Japan, Vietnam, Brunei, Philippines.</p>
      <p>We can provide local billing in Australia, New Zealand, China, Indonesia, Singapore, Malaysia, Thailand, Hong Kong, Japan, Philippines and Vietnam.</p>
    </div>
    <span class="badge" style="left:128px"></span><span class="badge" style="left:152px"></span><span class="badge" style="left:176px"></span>
    <span class="badge" style="left:199px;width:8px;height:6px;top:133px;background:#444;border:none;border-radius:3px"></span>
  </section>

  <section class="slide solutions" style="left:802px;top:336px">
    <h2 class="heading"><span class="lead">OUR</span> SOLUTIONS</h2>
    <svg class="sol-icon" style="left:35px" viewBox="0 0 32 32"><g fill="none" stroke="#2b3a8f" stroke-width=".9"><rect x="10" y="8" width="12" height="5"/><rect x="10" y="14" width="12" height="5"/><rect x="10" y="20" width="12" height="5"/><circle cx="12" cy="10.5" r=".6"/><circle cx="12" cy="16.5" r=".6"/><circle cx="12" cy="22.5" r=".6"/></g></svg>
    <svg class="sol-icon" style="left:124px" viewBox="0 0 32 32"><g fill="none" stroke="#2b3a8f" stroke-width="1"><path d="M9 13h4l5-4v14l-5-4H9z"/><path d="M21 12c2 2 2 6 0 8M23.5 10c3 3 3 9 0 12"/></g></svg>
    <svg class="sol-icon" style="left:204px" viewBox="0 0 32 32"><g fill="none" stroke="#2b3a8f" stroke-width="1"><rect x="10" y="14" width="12" height="10" rx="1"/><path d="M12.5 14v-3a3.5 3.5 0 0 1 7 0v3"/><path d="M16 18v3"/></g></svg>
    <ul class="sol-col" style="left:27px"><h4>IT INFRASTRUCTURE</h4><li>Design</li><li>Fibre &amp; Copper Cabling</li><li>UPS</li><li>Network Equipment</li><li>Network Engineering Services</li><li>Server Room Equipment</li><li>PABX &amp; Telephony Systems</li><li>Wireless</li></ul>
    <ul class="sol-col" style="left:122px"><h4>AUDIO VISUAL</h4><li>Design</li><li>Display Screens</li><li>Video Conference Solutions</li><li>Meeting Room Control Systems</li><li>Sound Systems</li><li>Audio Cabling</li></ul>
    <ul class="sol-col" style="left:204px"><h4>SECURITY</h4><li>Design</li><li>Card Access</li><li>CCTV</li><li>Alarm Systems</li></ul>
    <p class="abs" style="left:96px;top:133px;font-size:2.4px">Other brands can also be supplied to meet client specifications or budget requirements</p>
    <div class="foot-line"></div><div class="mark foot-mark">NORTHVALE</div>
  </section>

  <section class="slide brands" style="left:132px;top:536px">
    <h2 class="heading"><span class="lead">SUP</span>PLY &amp; INSTALL ALL LEADING CABLING BRANDS</h2>
    <div class="brand" style="left:22px;top:29px">CONTROLA</div>
    <div class="brand-box" style="left:17px;top:39px;width:79px">AV presentation, room scheduling<br>and room control systems</div>
    <div class="brand" style="left:165px;top:37px;font-size:6px">NETVIA</div>
    <div class="brand" style="left:210px;top:37px;font-size:6px">CONFERA</div>
    <div class="brand-box" style="left:158px;top:47px;width:100px">Video Conferencing Solutions</div>
    <div class="brand" style="left:28px;top:60px;font-size:10px">LUMARO</div>
    <div class="brand-box" style="left:17px;top:71px;width:79px">AV Control systems for video walls,<br>wireless presentation</div>
    <div class="screen" role="img" aria-label="Display screen showing a city skyline at night"></div>
    <p class="abs" style="left:105px;top:104px;font-size:4px;line-height:4.6px;color:#555;text-align:center;width:46px">Any size or brand of display screens</p>
    <div class="brand" style="left:167px;top:74px">SONORA</div>
    <div class="brand" style="left:228px;top:74px;font-size:6px">TONVIA</div>
    <div class="brand-box" style="left:158px;top:84px;width:100px">Speakers</div>
    <div class="brand" style="left:50px;top:88px;font-size:6px">ORCHARD</div>
    <div class="brand-box" style="left:17px;top:101px;width:79px">Install &amp; Mount tablets for meeting<br>room booking systems, visitor registration</div>
    <div class="brand" style="left:162px;top:103px;font-size:6.5px">VOCALIS</div>
    <div class="brand" style="left:221px;top:103px;font-size:5px;font-weight:500">DSIGNAL</div>
    <div class="brand-box" style="left:158px;top:113px;width:46px">Microphones, headsets</div>
    <div class="brand-box" style="left:215px;top:113px;width:43px">Audio Processors</div>
    <p class="abs" style="left:135px;top:131px;font-size:2.4px">Other brands can also be supplied to meet client corporate specifications or budget requirements</p>
    <div class="foot-line"></div><div class="mark foot-mark">NORTHVALE</div>
  </section>

  <section class="slide break" style="left:467px;top:536px">
    <svg class="abs" style="left:108px;top:18px" width="52" height="60" viewBox="0 0 52 60"><g fill="none" stroke="#fff" stroke-width="2.4" stroke-linecap="round"><path d="M16 4c-3 4 3 7 0 12M24 2c-3 4 3 7 0 12M32 4c-3 4 3 7 0 12"/><path d="M8 26h32v10a14 14 0 0 1-14 14h-4A14 14 0 0 1 8 36z"/><path d="M40 30h3a5 5 0 0 1 0 10h-4"/><path d="M12 38c2 5 6 7 12 7"/></g></svg>
    <div class="abs" style="left:84px;top:95px;width:99px;height:.6px;background:#8b97d4"></div>
    <div class="lets">LET'S TAKE</div>
    <div class="big">A BREAK</div>
    <div class="mins">15 MINUTES PLEASE</div>
  </section>

  <section class="slide team" style="left:802px;top:536px">
    <h2 class="heading"><span class="lead">OUR</span> TEAM</h2>
    <svg class="abs" style="left:0;top:0" width="267" height="150" viewBox="0 0 267 150"><g stroke="#f7941d" stroke-width=".7" fill="none"><path d="M157 43v6M80 49h164M80 49v4M127 49v4M179 49v4M226 49v4"/><path d="M85 62v60M135 62v28M183 62v60M230 62v60"/><path d="M85 80h4M85 94h4M85 108h4M85 122h4M135 80h4M135 90h4M183 80h4M183 94h4M183 108h4M183 122h4M230 80h4M230 94h4M230 108h4M230 122h4"/></g><circle cx="157" cy="38" r="5" fill="#f7941d" stroke="#fff" stroke-width="1.2"/><circle cx="157" cy="38" r="6" fill="none" stroke="#f7941d" stroke-width=".6"/></svg>
    <div class="pname" style="left:145px;top:24px">Arun Mehta<small>General Manager</small></div>
    <div class="person" role="img" aria-label="Portrait photo of managing director" style="left:30px;top:32px"></div>
    <div class="pname" style="left:25px;top:53px">Daniel Cho<small>Managing Director</small></div>
    <div class="person" role="img" aria-label="Portrait photo of HR and accounts manager" style="left:30px;top:70px"></div>
    <div class="pname" style="left:25px;top:91px">Daniel Cho<small>HR &amp; Accounts Manager</small></div>
    <div class="person" role="img" aria-label="Portrait photo of finance lead" style="left:30px;top:106px"></div>
    <div class="pname" style="left:25px;top:127px">Daniel Cho<small>Finance</small></div>
    <div class="pname" style="left:70px;top:55px">Arun Mehta<small>Technical Leads</small></div>
    <div class="pname" style="left:119px;top:55px">Arun Mehta<small>Client Delivery</small></div>
    <div class="pname" style="left:168px;top:55px">Arun Mehta<small>Sales Operations</small></div>
    <div class="pname" style="left:216px;top:55px">Arun Mehta<small>Sales Teams</small></div>
    <div class="pname" style="left:89px;top:77px">Arun Mehta<small>Audio Visual</small></div>
    <div class="pname" style="left:89px;top:91px">Arun Mehta<small>Structured Cabling</small></div>
    <div class="pname" style="left:89px;top:105px">Arun Mehta<small>Network Engineering</small></div>
    <div class="pname" style="left:89px;top:119px">Arun Mehta<small>CAD &amp; Documentation</small></div>
    <div class="pname" style="left:139px;top:77px">Arun Mehta<small>Service Management</small></div>
    <div class="pname" style="left:139px;top:87px">Arun Mehta<small>Dedicated Project Managers</small></div>
    <div class="pname" style="left:187px;top:77px">Arun Mehta<small>Audio Visual</small></div>
    <div class="pname" style="left:187px;top:91px">Arun Mehta<small>Audio Visual</small></div>
    <div class="pname" style="left:187px;top:105px">Arun Mehta<small>Audio Visual</small></div>
    <div class="pname" style="left:187px;top:119px">Arun Mehta<small>Audio Visual</small></div>
    <div class="pname" style="left:234px;top:77px">Arun Mehta<small>Regional Accounts</small></div>
    <div class="pname" style="left:234px;top:91px">Arun Mehta<small>Australia / NZ</small></div>
    <div class="pname" style="left:234px;top:105px">Arun Mehta<small>Singapore / Malaysia</small></div>
    <div class="pname" style="left:234px;top:119px">Arun Mehta<small>Hong Kong / North Asia</small></div>
    <div class="foot-line"></div><div class="mark foot-mark">NORTHVALE</div>
  </section>

  <section class="slide clients" style="left:132px;top:736px">
    <h2 class="heading"><span class="lead">CLIE</span>NTS</h2>
    <svg class="abs" style="left:14px;top:41px" width="60" height="56" viewBox="0 0 60 56"><g fill="none" stroke="#2b3a8f" stroke-width="3.2" stroke-linecap="round"><circle cx="22" cy="15" r="11"/><path d="M3 54c0-13 8-22 19-22s19 9 19 22"/><path d="M35 5a11 11 0 0 1 0 21"/><path d="M44 32c8 3 13 11 13 22"/></g></svg>
    <div class="text">
      <p>Our clients range from hotels, large multi-national companies to any corporate office with an intelligent approach to their IT needs. As a business partner of leading hardware and software manufacturers, Northvale can offer a wide range of products and services to cater for varying budgets and technology requirements.</p>
      <p style="margin-top:3px">We can either work direct with the Client or through your Project Manager or Designer.</p>
    </div>
    <div class="link"><span style="color:#6b76b5">Visit our website</span> <b>www.northvale.com</b><br>to view our client portfolio</div>
    <div class="foot-line"></div><div class="mark foot-mark">NORTHVALE</div>
  </section>

  <section class="slide projects" style="left:467px;top:736px">
    <h2 class="heading"><span class="lead">PRO</span>JECT EXPERIENCE</h2>
    <div class="proj" style="left:16px">
      <div class="proj-img" role="img" aria-label="Client office interior photograph"><span><small>Client</small>ORCHARD LABS</span></div>
      <p class="meta">Project: Singapore, Vietnam, Auckland, Indonesia Corporate Offices Ongoing projects since 2017<br>Project Values: $2M+</p>
      <ul><li>Design, supply and install of AV equipment including:</li><li class="b">Installation and Mounting of tablets</li><li class="b">Video Conferencing</li><li class="b">Training Room with Projector &amp; Integrated Speakers</li><li class="b">Boardroom Automation</li><li class="b">Room control systems</li></ul>
    </div>
    <div class="proj" style="left:97px">
      <div class="proj-img" role="img" aria-label="Office tower photograph"><span><small>Client</small>VELTERA</span></div>
      <p class="meta">Project: Philippines New Corporate Office, North Exchange, 2 Floors November 2018 to January 2019</p>
      <ul><li>Design, supply and install of AV equipment including:</li><li class="b">Structured Cabling Design</li><li>– Copper cabling products</li><li>– 500 data points</li><li>– Server room equipment</li><li class="b">AV design for 6 room types including boardroom, training, break out and meeting rooms.</li><li>– Video Conferencing</li><li>– Audio and control systems, speakers</li><li>– Wireless microphones</li></ul>
    </div>
    <div class="proj" style="left:178px">
      <div class="proj-img" role="img" aria-label="Office building photograph"><span><small>Client</small>MERIDIAN</span></div>
      <p class="meta">Project: Singapore Corporate Office, Harbour Point, July 2017<br>Project Values: $600K</p>
      <ul><li>Design, supply and install of structured cabling and audio visual equipment including:</li><li class="b">Structured Cabling Design</li><li>– Copper cabling products</li><li>– 900 data points</li><li>– Server room equipment</li><li class="b">AV design for 7 room types including boardrooms, training, breakout and 10 pax meeting rooms.</li><li>– Wireless share units</li><li>– Wireless</li><li>– Video Conferencing</li><li>– Audio and control systems, speakers</li><li>– Wireless microphones</li></ul>
    </div>
  </section>

  <section class="slide projects" style="left:802px;top:736px">
    <h2 class="heading"><span class="lead">PRO</span>JECT EXPERIENCE</h2>
    <div class="proj" style="left:16px">
      <div class="proj-img" role="img" aria-label="Client office interior photograph"><span><small>Client</small>RIDELINK</span></div>
      <p class="meta">Project: Singapore, Vietnam, Auckland, Indonesia Corporate Offices Ongoing projects since 2017<br>Project Values: $2M+</p>
      <ul><li>Design, supply and install of AV equipment including:</li><li class="b">Installation and Mounting of tablets</li><li class="b">Video Conferencing</li><li class="b">Training Room with Projector &amp; Integrated Speakers</li><li class="b">Boardroom Automation</li><li class="b">Room control systems</li></ul>
    </div>
    <div class="proj" style="left:97px">
      <div class="proj-img" role="img" aria-label="Office tower photograph"><span><small>Client</small>VELTERA</span></div>
      <p class="meta">Project: Philippines New Corporate Office, North Exchange, 2 Floors November 2018 to January 2019</p>
      <ul><li>Design, supply and install of AV equipment including:</li><li class="b">Structured Cabling Design</li><li>– Copper cabling products</li><li>– 500 data points</li><li>– Server room equipment</li><li class="b">AV design for 6 room types including boardroom, training, break out and meeting rooms.</li><li>– Video Conferencing</li><li>– Audio and control systems, speakers</li><li>– Wireless microphones</li></ul>
    </div>
    <div class="proj" style="left:178px">
      <div class="proj-img" role="img" aria-label="Office building photograph"><span><small>Client</small>MERIDIAN</span></div>
      <p class="meta">Project: Singapore Corporate Office, Harbour Point, July 2017<br>Project Values: $600K</p>
      <ul><li>Design, supply and install of structured cabling and audio visual equipment including:</li><li class="b">Structured Cabling Design</li><li>– Copper cabling products</li><li>– 900 data points</li><li>– Server room equipment</li><li class="b">AV design for 7 room types including boardrooms, training, breakout and 10 pax meeting rooms.</li><li>– Wireless share units</li><li>– Wireless</li><li>– Video Conferencing</li><li>– Audio and control systems, speakers</li><li>– Wireless microphones</li></ul>
    </div>
  </section>

  <section class="slide safety" style="left:132px;top:937px">
    <h2 class="heading"><span class="lead">HEA</span>LTH &amp; SAFETY STATEMENT</h2>
    <svg class="abs" style="left:14px;top:49px" width="58" height="70" viewBox="0 0 58 70"><path d="M29 3 5 12v20c0 17 10 29 24 35 14-6 24-18 24-35V12z" fill="none" stroke="#2b3a8f" stroke-width="3.6" stroke-linejoin="round"/><path d="M17 35l9 9 16-18" fill="none" stroke="#f7941d" stroke-width="4.2" stroke-linecap="round" stroke-linejoin="round"/></svg>
    <p class="intro-line">As part of the Northvale Health &amp; Safety Policy, we will:-</p>
    <ul class="bullets">
      <li>Provide health &amp; safety policy training to all staff.</li>
      <li>Ensure all staff are competent and adequately resourced to address the health and safety issues likely to be involved on site.</li>
      <li>Check that clients are aware of their duties.</li>
      <li>When carrying out design and build work, avoid foreseeable risks to those involved in the construction and future use of the equipment, and in doing so, they should estimate hazards and reduce risk associated with those hazards which remain.</li>
      <li>Provide adequate information about any significant risks associated with the design and build.</li>
      <li>Coordinate work with that of others in order to improve the way in which risks are managed and controlled.</li>
      <li>In carrying out those duties, our designers and installers need to consider the hazards any risks to those who carry out construction work including demolition.</li>
      <li>Use a structure designed as a place of work may be affected by such work, for example customers or general public.</li>
    </ul>
    <div class="foot-line"></div><div class="mark foot-mark">NORTHVALE</div>
  </section>

  <section class="slide why" style="left:467px;top:937px">
    <h2 class="heading"><span class="lead">WHY</span> CHOOSE NORTHVALE?</h2>
    <div class="handshake" role="img" aria-label="Handshake illustration in blue line art"></div>
    <ul class="bullets">
      <li>With our partners, breadth and depth of experience, we are able to offer you choice for a competitive price with a quality solution and service throughout Asia Pacific markets.</li>
      <li>Our team has experience in Audio Visual and IT Infrastructure design &amp; build, both in Singapore and across Asia Pacific for large multi-national organisations. We support leading global companies regionally such as Orchard Labs, RideLink, and Workhive.</li>
      <li>Vast experience installing Controla, Signex, Lumaro, Clarivo, Tonehall, Roomtone, Linqo, Dsignal, Vocalis, Tonvia, all display brands, touchscreen meeting room boards, and Nuvora, Confera &amp; Netvia conferencing solutions.</li>
      <li>Top level management maintain a hands-on involvement in projects.</li>
      <li>Committed team who understand the need for effective communication and in non-English speaking markets.</li>
    </ul>
    <div class="foot-line"></div><div class="mark foot-mark">NORTHVALE</div>
  </section>

  <section class="slide thanks" style="left:802px;top:937px">
    <div class="title">THANK YOU</div>
    <div class="mark">NORTHVALE</div>
    <div class="office" style="left:8px"><div class="flag" role="img" aria-label="Singapore flag"></div>Singapore<br>+65 6100 2040</div>
    <div class="office" style="left:58px"><div class="flag" role="img" aria-label="Hong Kong flag"></div>Hong Kong<br>+852 3100 2040</div>
    <div class="office" style="left:112px"><div class="flag" role="img" aria-label="Australia flag" style="background:#1f3a8f"></div>Sydney<br>+61 2 8100 2040</div>
    <div class="office" style="left:165px"><div class="flag" role="img" aria-label="New Zealand flag" style="background:#1f3a8f"></div>Auckland<br>+64 9 910 2040</div>
    <div class="office" style="left:218px"><div class="flag" role="img" aria-label="Malaysia flag" style="background:linear-gradient(180deg,#cc1f2f 50%,#fff 50%)"></div>Malaysia<br>+60 11 1002 040</div>
    <div class="rule"></div>
    <div class="web" style="left:60px">www.northvale.com</div>
    <div class="web" style="left:156px">info@northvale.com</div>
  </section>

</div>
</body>
</html>
```